Court Heritage Trust Business Card

We need a business card design for the Court Heritage Trust. It is a non-profit organization that promotes environmental awareness and activism within the tennis community. It will include our newly designed logo. It needs to be modern yet with an elegant business feel. The market we deal with is upscale with discerning taste. Must convey a sense of seriousness that people can trust, while inspiring their highest values to create a better world.
Target Market(s)
Upscale market of tennis, business, and environmental enthusiasts
Industry/Entity Type
Non-Profit
Requirements
Must have
- Must have an elegant look, be easy to read and convey seriousness of purpose.
Show where you will place the name, title, address, email and phone number on front of the card.
Note: We have included both versions of our new logo. Feel free to use either or both. We are not sure which will be ideal for a business card. The files are in jpg. We can supply other formats if they will be easier to work with.
Nice to have
- The back side should have the following:
Printed by "PLIX" on:
100% recycled post consumer waste
100% recyclable and biodegradable
Sustainable source, Elemental Chlorine Free (ECF)
Manufactured using wind power
Include the plix logo from the images section.

```html
<!DOCTYPE html>
<html lang="en">
<head>
<meta charset="utf-8">
<title>Court Heritage Trust – Business Card</title>
<link href="https://fonts.googleapis.com/css2?family=Open+Sans:wght@400;600;700;800&display=swap" rel="stylesheet">
<style>
  :root {
    --backdrop: #9a9a9a;
    --card: #f7f7f7;
    --card-shade: #e6e6e6;
    --teal: #136a8a;
    --ink: #2f2f2f;
    --muted: #4a4a4a;
  }
  * { box-sizing: border-box; margin: 0; padding: 0; }
  html, body { width: 1200px; height: 896px; overflow: hidden; }
  body {
    background: var(--backdrop);
    font-family: "Open Sans", Arial, sans-serif;
    display: flex;
    align-items: center;
    justify-content: center;
    gap: 40px;
  }
  .card {
    position: relative;
    width: 540px;
    height: 309px;
    background: linear-gradient(135deg, #ffffff 0%, var(--card) 55%, var(--card-shade) 100%);
    overflow: hidden;
    box-shadow: 0 6px 18px rgba(0,0,0,0.25);
  }
  .card-accent { position: absolute; inset: 0; width: 100%; height: 100%; }

  /* Front */
  .brand {
    position: absolute; top: 30px; left: 26px;
    display: flex; align-items: center; gap: 12px;
  }
  .brand-dot {
    width: 40px; height: 40px; border-radius: 50%;
    background: var(--teal);
  }
  .brand-name {
    color: var(--teal); font-weight: 600; font-size: 22px;
    letter-spacing: 0.5px; text-transform: uppercase;
  }
  .name-block {
    position: absolute; top: 110px; left: 0;
    display: flex; align-items: stretch;
  }
  .name-marker { width: 34px; height: 54px; background: var(--teal); }
  .name-text { padding-left: 14px; padding-top: 4px; }
  .person-name {
    font-weight: 800; font-size: 26px; color: var(--ink);
    text-transform: uppercase; line-height: 1;
  }
  .person-title {
    margin-top: 6px; font-size: 12px; color: var(--teal);
    letter-spacing: 5px; text-transform: uppercase;
  }
  .contact-list {
    position: absolute; right: 36px; bottom: 22px;
    list-style: none; width: 190px;
  }
  .contact-item {
    display: flex; align-items: flex-start; gap: 10px;
    font-size: 11.5px; font-weight: 600; color: var(--muted);
    line-height: 1.3; margin-top: 6px;
  }
  .contact-icon { width: 14px; height: 14px; flex: none; fill: var(--teal); }

  /* Back */
  .back-brand {
    position: absolute; top: 100px; left: 0; right: 0;
    display: flex; flex-direction: column; align-items: center; gap: 12px;
  }
  .back-brand .brand-dot { width: 56px; height: 56px; }
  .back-brand .brand-name { font-size: 18px; }
  .social-row {
    position: absolute; left: 36px; right: 60px; bottom: 34px;
    display: flex; justify-content: space-between; list-style: none;
  }
  .social-item {
    display: flex; align-items: center; gap: 8px;
    font-size: 12px; color: var(--muted);
  }
  .social-mark { width: 16px; height: 16px; background: var(--teal); }
  .edge-tab {
    position: absolute; right: 0; top: 216px;
    width: 14px; height: 36px; background: var(--teal);
  }
</style>
</head>
<body>

<section class="card card-front" aria-label="Business card front">
  <svg class="card-accent" viewBox="0 0 540 309" preserveAspectRatio="none" aria-hidden="true">
    <path d="M0,0 L540,0 L540,30 Q300,8 0,6 Z" fill="var(--teal)"/>
  </svg>
  <div class="brand">
    <span class="brand-dot"></span>
    <span class="brand-name">Court Heritage Trust</span>
  </div>
  <div class="name-block">
    <span class="name-marker"></span>
    <div class="name-text">
      <p class="person-name">Daniel Harlow</p>
      <p class="person-title">General Manager</p>
    </div>
  </div>
  <ul class="contact-list">
    <li class="contact-item">
      <svg class="contact-icon" viewBox="0 0 16 16"><path d="M8 1 L15 7.5 L13 7.5 L13 15 L9.5 15 L9.5 10.5 L6.5 10.5 L6.5 15 L3 15 L3 7.5 L1 7.5 Z"/></svg>
      <span>27 Baseline Ave, Suite 4<br>Westgate</span>
    </li>
    <li class="contact-item">
      <svg class="contact-icon" viewBox="0 0 16 16"><circle cx="8" cy="8" r="6.5" fill="none" stroke="var(--teal)" stroke-width="1.4"/><path d="M1.5 8 H14.5 M8 1.5 V14.5" stroke="var(--teal)" stroke-width="1.2"/><ellipse cx="8" cy="8" rx="3" ry="6.5" fill="none" stroke="var(--teal)" stroke-width="1.2"/></svg>
      <span>www.yourwebsite.com</span>
    </li>
    <li class="contact-item">
      <svg class="contact-icon" viewBox="0 0 16 16"><rect x="1" y="3" width="14" height="10" rx="1"/><path d="M1.5 3.8 L8 9 L14.5 3.8" fill="none" stroke="#fff" stroke-width="1.2"/></svg>
      <span>yourname@email.com</span>
    </li>
    <li class="contact-item">
      <svg class="contact-icon" viewBox="0 0 16 16"><path d="M4 1 L6.5 4.5 L5 6.5 Q6.5 9.5 9.5 11 L11.5 9.5 L15 12 L13 15 Q3 13.5 1 3 Z"/></svg>
      <span>012 345 6789</span>
    </li>
  </ul>
</section>

<section class="card card-back" aria-label="Business card back">
  <svg class="card-accent" viewBox="0 0 540 309" preserveAspectRatio="none" aria-hidden="true">
    <path d="M250,0 L540,0 L540,70 Q450,22 250,0 Z" fill="var(--teal)"/>
  </svg>
  <div class="back-brand">
    <span class="brand-dot"></span>
    <span class="brand-name">Court Heritage Trust</span>
  </div>
  <ul class="social-row">
    <li class="social-item"><span class="social-mark"></span>yourname</li>
    <li class="social-item"><span class="social-mark"></span>@yourname</li>
    <li class="social-item"><span class="social-mark"></span>yourname</li>
  </ul>
  <span class="edge-tab"></span>
</section>

</body>
</html>
```